Business Card for a Floral & Decorating Business

I would like to take my current logo and create a better business card. I am looking for elegance as I am a florist and event decorator. My logo has multiple colour options. I like colours like green, purple, pink and orange, I think I would like a white card, open to black back ground. I want it to feel elegant and romantic. I like metallic lettering that maybe is indented in the paper, I also like glossy paper. I have a full logo already as well as a badge. I have attached both in multiple colours.m
Updates

Need extra days to review

Target Market(s)

Weddings, special events, floral customers

Industry/Entity Type

Floral and decorating

Contact Information for Business Card

Phone number, email, instagram, facebook, title, name, logo

Font styles to use
Script

Requirements
Nice to have
• Elegant

```html
<!DOCTYPE html>
<html lang="en">
<head>
<meta charset="utf-8">
<title>Laurel Vale Business Card</title>
<link rel="stylesheet" href="https://fonts.googleapis.com/css2?family=Libre+Baskerville:wght@400;700&family=Montserrat:wght@400&display=swap">
<style>
  :root {
    --backdrop: #979797;
    --berry: #9b4560;
    --berry-soft: #c98fa1;
    --paper: #ffffff;
    --ink: #2a2a2a;
  }
  * { margin: 0; padding: 0; box-sizing: border-box; }
  html, body { width: 1200px; height: 1059px; overflow: hidden; }
  body { background: var(--backdrop); position: relative; font-family: "Montserrat", sans-serif; }

  .card { position: absolute; border-radius: 18px; overflow: hidden; }
  .card-front { left: 256px; top: 89px; width: 687px; height: 390px; background: var(--paper); }
  .card-back { left: 253px; top: 569px; width: 694px; height: 394px; background: var(--berry); }

  .brand-name {
    font-family: "Libre Baskerville", serif; font-weight: 400;
    color: var(--berry); letter-spacing: 0.06em; white-space: nowrap;
  }
  .front-brand { position: absolute; left: 30px; top: 62px; font-size: 36px; }

  .accent-bar { position: absolute; left: 0; top: 157px; width: 16px; height: 40px; background: var(--berry); }
  .person-name {
    position: absolute; left: 30px; top: 152px;
    font-family: "Libre Baskerville", serif; font-weight: 700;
    font-size: 25px; color: var(--berry); letter-spacing: 0.01em;
  }
  .person-title { position: absolute; left: 30px; top: 182px; font-size: 17px; color: var(--ink); }
  .address { position: absolute; left: 30px; top: 222px; font-size: 17px; line-height: 21px; color: var(--ink); }
  .contact-list { position: absolute; left: 30px; top: 280px; list-style: none; }
  .contact-list li { display: flex; align-items: center; height: 27px; font-size: 17px; color: var(--ink); }
  .contact-list svg { width: 13px; height: 13px; margin-right: 6px; fill: var(--berry); flex: none; }

  .front-monogram {
    position: absolute; left: 420px; top: 26px; width: 238px; height: 341px;
    border-radius: 10px;
    background: linear-gradient(160deg, #f4e4e9 0%, var(--berry-soft) 100%);
  }

  .back-monogram {
    position: absolute; left: 310px; top: 55px; width: 81px; height: 114px;
    border-radius: 6px;
    background: linear-gradient(160deg, rgba(255,255,255,0.35), rgba(255,255,255,0.15));
  }
  .back-brand {
    position: absolute; left: 0; right: 0; top: 188px; text-align: center;
    font-size: 52px; color: var(--paper);
  }
  .social-row { position: absolute; left: 291px; top: 328px; display: flex; gap: 11px; }
  .social-row span { width: 29px; height: 29px; border-radius: 6px; background: var(--paper); }
</style>
</head>
<body>
  <section class="card card-front">
    <div class="brand-name front-brand">Laurel Vale</div>
    <div class="accent-bar"></div>
    <h1 class="person-name">MARA ELLISON</h1>
    <p class="person-title">CEO/Founder</p>
    <p class="address">42 Orchard Lane Suite B<br>Fernbrook CA, 90218</p>
    <ul class="contact-list">
      <li><svg viewBox="0 0 24 24"><path d="M6.6 10.8a15.1 15.1 0 0 0 6.6 6.6l2.2-2.2a1 1 0 0 1 1-.25 11.4 11.4 0 0 0 3.6.57 1 1 0 0 1 1 1V20a1 1 0 0 1-1 1A17 17 0 0 1 3 4a1 1 0 0 1 1-1h3.5a1 1 0 0 1 1 1c0 1.25.2 2.45.57 3.57a1 1 0 0 1-.25 1z"/></svg>(555) 014-2398</li>
      <li><svg viewBox="0 0 24 24"><path d="M2 5h20v2l-10 6L2 7z M2 9l10 6 10-6v10H2z"/></svg>hello@laurelvale.com</li>
      <li><svg viewBox="0 0 24 24"><path d="M12 2a10 10 0 1 0 0 20 10 10 0 0 0 0-20zm0 2c.9 0 2.2 1.8 2.8 5H9.2C9.8 5.8 11.1 4 12 4zM4.3 11h3.2c0 .7 0 1.3.1 2H4.3a8 8 0 0 1 0-2zm.8 4h2.8c.3 1.4.8 2.6 1.4 3.6A8 8 0 0 1 5.1 15zm2.8-6H5.1a8 8 0 0 1 4.2-3.6C8.7 6.4 8.2 7.6 7.9 9zM12 20c-.9 0-2.2-1.8-2.8-5h5.6c-.6 3.2-1.9 5-2.8 5zm3.2-7H8.8a17 17 0 0 1 0-2h6.4a17 17 0 0 1 0 2zm-.5 5.6c.6-1 1.1-2.2 1.4-3.6h2.8a8 8 0 0 1-4.2 3.6zm1.8-5.6c.1-.7.1-1.3.1-2h3.2a8 8 0 0 1 0 2zm-.4-4c-.3-1.4-.8-2.6-1.4-3.6A8 8 0 0 1 18.9 9z"/></svg>www.laurelvale.com</li>
    </ul>
    <div class="front-monogram" role="img" aria-label="Large floral monogram illustration with line-drawn flowers and leaves"></div>
  </section>

  <section class="card card-back">
    <div class="back-monogram" role="img" aria-label="Small floral monogram illustration in white line art"></div>
    <div class="brand-name back-brand">Laurel Vale</div>
    <div class="social-row" aria-label="Social media links">
      <span></span><span></span><span></span>
    </div>
  </section>
</body>
</html>
```